Velvet Quarry Brochure

I would like to design an e-brochure to be sent to a particular fashion designer that we choose to invite to be featured on our platform. The brochure should reflect the existing brand image of the website. The brochure will probably have no more than four to five pages and will include the following information

1) Cover Page

2) About Us

3) Our Unique Edge

4) Member Benefits

5) Prices

6) Contact
Updates

hello designers think some people are confused about what the brochure is about i have uploaded a file with the sample text - hope this helps

Reason: Hi everyone I have extended the deadline as i have uploaded a text document for the brochure that should assist with thinking about the design. please email if you have questions

Hi I have got feedback that the document wasn't uploaded properly - the sample text to work with is now uploaded on docx format Thanks

Target Market(s)

Fashion designers

Industry/Entity Type

Fashion

Requirements
Must have
• Must be cool, edgy , contemporary and inviting

please see website www.velvetquarry-example.com - as look and feel should tie in with that

photos and art work can be used from website and all our social media pages

```html
<!DOCTYPE html>
<html lang="en">
<head>
<meta charset="utf-8">
<title>Velvet Quarry Brochure – About Us &amp; Prices</title>
<link rel="stylesheet" href="https://fonts.googleapis.com/css2?family=Kaushan+Script&family=Questrial&family=Arimo:wght@400;700&display=swap">
<style>
  :root {
    --ink: #1c1c1c;
    --charcoal: #333333;
    --paper: #eef1f0;
    --paper-light: #f6f7f7;
    --band: #d7d9dc;
    --band-dark: #cfd1d4;
    --white: #ffffff;
    --photo-night: #2a3552;
    --photo-night-2: #4a3a55;
    --photo-bag: #c23a48;
    --product: #8a7d70;
  }
  * { box-sizing: border-box; margin: 0; padding: 0; }
  html, body { width: 1200px; height: 849px; overflow: hidden; background: var(--paper); }
  .spread { position: relative; width: 1200px; height: 849px; font-family: "Questrial", sans-serif; color: var(--ink); overflow: hidden; }

  .page-left { position: absolute; left: 0; top: 0; width: 600px; height: 849px; background: var(--paper); overflow: hidden; }
  .page-left svg { position: absolute; left: 0; top: 0; }

  .script { font-family: "Kaushan Script", cursive; font-weight: 400; }

  .about-title { position: absolute; left: 520px; top: 72px; transform: translate(-50%, -50%) rotate(50deg); font-size: 36px; white-space: nowrap; }
  .about-copy { position: absolute; left: 312px; top: 462px; width: 740px; transform: translate(-50%, -50%) rotate(-44.6deg); font-size: 12px; line-height: 15px; text-align: center; }
  .edge-title { position: absolute; left: 155px; top: 738px; transform: translate(-50%, -50%) rotate(-45deg); font-size: 38px; white-space: nowrap; }
  .edge-copy { position: absolute; left: 190px; top: 744px; width: 405px; font-size: 13px; line-height: 16px; text-align: justify; }

  .page-right { position: absolute; left: 600px; top: 0; width: 600px; height: 849px; background: var(--white); overflow: hidden; }
  .page-right svg { position: absolute; left: 0; top: 0; }
  .benefits-title { position: absolute; left: 20px; top: 66px; font-size: 40px; color: var(--white); transform: rotate(-6deg); transform-origin: left center; }
  .benefits-list { position: absolute; left: 14px; top: 162px; width: 578px; font-size: 12.5px; line-height: 15px; list-style: disc; padding-left: 14px; text-align: justify; transform: rotate(-4deg); transform-origin: left top; }
  .prices-title { position: absolute; left: 28px; top: 298px; font-size: 34px; }
  .prices-note { position: absolute; font-size: 13px; white-space: nowrap; }
  .prices-note::before { content: "•"; margin-right: 8px; }

  .product-grid { position: absolute; left: 47px; top: 385px; display: grid; grid-template-columns: 147px 147px 147px; column-gap: 24px; row-gap: 22px; }
  .product-grid .product:nth-child(3n) { transform: translateX(16px); }
  .product { width: 147px; height: 139px; text-align: center; font-family: "Arimo", sans-serif; }
  .product-photo { height: 100px; border: 2px solid var(--ink); background: var(--white); display: flex; justify-content: center; align-items: flex-end; }
  .product-photo span { display: block; width: 46px; height: 88px; border-radius: 20px 20px 4px 4px; background: linear-gradient(180deg, #222 0%, var(--product) 45%, #2a2a2a 100%); }
  .product-name { margin: 7px -10px 0; font-size: 11.5px; line-height: 15px; white-space: nowrap; }
  .product-price { font-size: 12px; line-height: 16px; font-weight: 700; }
</style>
</head>
<body>
<main class="spread">

  <section class="page-left">
    <svg width="600" height="849" viewBox="0 0 600 849">
      <defs>
        <clipPath id="hero-area"><polygon points="0,0 440,0 565,150 0,710"/></clipPath>
        <linearGradient id="night" x1="0" y1="0" x2="1" y2="1">
          <stop offset="0" stop-color="var(--photo-night)"/>
          <stop offset="0.6" stop-color="var(--photo-night-2)"/>
          <stop offset="1" stop-color="#1e2433"/>
        </linearGradient>
        <linearGradient id="bag" x1="0" y1="0" x2="1" y2="1">
          <stop offset="0" stop-color="#f4f4f4"/>
          <stop offset="0.5" stop-color="#e7d9cf"/>
          <stop offset="1" stop-color="var(--photo-bag)"/>
        </linearGradient>
      </defs>
      <polygon class="band" points="0,710 600,116 600,360 0,952" fill="var(--band)"/>
      <g clip-path="url(#hero-area)">
        <rect width="600" height="720" fill="url(#night)" role="img" aria-label="Model in a dark blazer, cropped tee and striped trousers holding a red bag on a night street"/>
        <g stroke="var(--white)" stroke-width="9">
          <line x1="-300" y1="150" x2="500" y2="950"/>
          <line x1="-300" y1="-120" x2="600" y2="780"/>
          <line x1="-100" y1="-200" x2="700" y2="600"/>
          <line x1="100" y1="-200" x2="800" y2="500"/>
          <line x1="-100" y1="300" x2="400" y2="-200"/>
          <line x1="-100" y1="500" x2="600" y2="-200"/>
        </g>
      </g>
      <polygon points="0,710 565,150 600,150 600,116 0,710" fill="var(--band-dark)"/>
      <line x1="0" y1="830" x2="600" y2="236" stroke="#9a9a9a" stroke-width="1.5" stroke-dasharray="7 7"/>
      <polygon points="230,725 600,360 600,725" fill="url(#bag)" role="img" aria-label="Red leather backpack with dragonfly print flap, shown alone and worn by a woman"/>
    </svg>

    <h2 class="about-title script">About Us</h2>
    <p class="about-copy">Velvet Quarry is an online destination for edgy, indie, global design. It is a celebration of fashion – fashion which represents creativity, expression and rebellion. We look all over the world for exciting and emerging design talent to find something that brings something of the designer and his or her part of the world to your part of the world.</p>
    <h2 class="edge-title script">Our Unique Edge</h2>
    <p class="edge-copy">We don’t slavishly follow seasons (after all it’s always summer somewhere right?), we don’t do here today gone tomorrow, fads and fast fashion, we don’t do labels for the sake of labels, we don’t do anything faux unless its faux fur. We value quality and good craftsmanship.</p>
  </section>

  <section class="page-right">
    <svg width="600" height="849" viewBox="0 0 600 849">
      <polygon points="0,160 600,95 600,240 0,300" fill="var(--paper-light)"/>
      <polygon points="0,300 600,240 600,375 0,375" fill="var(--band)"/>
      <polygon points="0,0 600,0 600,70 0,160" fill="var(--charcoal)"/>
    </svg>

    <h2 class="benefits-title script">Member Benefits</h2>
    <ul class="benefits-list">
      <li>We don’t slavishly follow seasons (after all it’s always summer somewhere right?),</li>
      <li>we don’t do here today gone tomorrow, fads and fast fashion, we don’t do labels for the sake of labels,</li>
      <li>we don’t do anything faux unless its faux fur. We value quality and good craftsmanship.</li>
      <li>We don’t slavishly follow seasons (after all it’s always summer somewhere right?), we don’t do here today gone tomorrow, fads and fast fashion, we don’t do labels for the sake of labels, we don’t do anything faux unless its faux fur. We value quality and good craftsmanship.</li>
    </ul>

    <h2 class="prices-title script">Prices</h2>
    <p class="prices-note" style="left:270px; top:332px;">we don’t do labels for the sake of labels, we don’t</p>
    <p class="prices-note" style="left:46px; top:354px;">we don’t do labels for the sake of labels, we don’t do anything faux unless its faux fur.</p>

    <div class="product-grid">
      <article class="product"><div class="product-photo" role="img" aria-label="Model wearing army print panel skirt"><span></span></div><p class="product-name">ARMY PRINT PANEL SKIRT</p><p class="product-price">£215.00</p></article>
      <article class="product"><div class="product-photo" role="img" aria-label="Model wearing army print panel skirt"><span></span></div><p class="product-name">ARMY PRINT PANEL SKIRT</p><p class="product-price">£215.00</p></article>
      <article class="product"><div class="product-photo" role="img" aria-label="Model wearing army print panel skirt"><span></span></div><p class="product-name">ARMY PRINT PANEL SKIRT</p><p class="product-price">£215.00</p></article>
      <article class="product"><div class="product-photo" role="img" aria-label="Model wearing army print panel skirt"><span></span></div><p class="product-name">ARMY PRINT PANEL SKIRT</p><p class="product-price">£215.00</p></article>
      <article class="product"><div class="product-photo" role="img" aria-label="Model wearing army print panel skirt"><span></span></div><p class="product-name">ARMY PRINT PANEL SKIRT</p><p class="product-price">£215.00</p></article>
      <article class="product"><div class="product-photo" role="img" aria-label="Model wearing army print panel skirt"><span></span></div><p class="product-name">ARMY PRINT PANEL SKIRT</p><p class="product-price">£215.00</p></article>
      <article class="product"><div class="product-photo" role="img" aria-label="Model wearing army print panel skirt"><span></span></div><p class="product-name">ARMY PRINT PANEL SKIRT</p><p class="product-price">£215.00</p></article>
      <article class="product"><div class="product-photo" role="img" aria-label="Model wearing army print panel skirt"><span></span></div><p class="product-name">ARMY PRINT PANEL SKIRT</p><p class="product-price">£215.00</p></article>
      <article class="product"><div class="product-photo" role="img" aria-label="Model wearing army print panel skirt"><span></span></div><p class="product-name">ARMY PRINT PANEL SKIRT</p><p class="product-price">£215.00</p></article>
    </div>
  </section>

</main>
</body>
</html>
```